Web Site Design For Real Estate Sales Project

The idea behind this project is pretty simple. I am putting my penthouse apartment up for sale and am trying to be creative in selling it.
Technically this will be pretty simple, it will be 3 pages but graphically this has to be as impressive as possible which is why I am trying Pixel Harbor.
The apartment is located in Barra Da Tijuca, Rio De Janeiro, Brazil. (This is where the 2016 Meridian Regatta will be held)
I am looking for an index page and 2 sub-pages. I am open to all kinds of designs and navigation's but it has to make an impression quickly with a professional and enticing design. The index page should make it obvious that there is a penthouse apartment for sale in Barra Da Tijuca ( suburb of Rio De Janeiro). The first sub page is about the Condominium where the apartment is located, the second sub page is about the apartment itself.
Here is a more detailed description of what the 3 pages should be about.
Index Page
This is the landing page and should make it obvious that there is an apartment for sale in Barra Da Tijuca, Rio De Janeiro with the following attributes
251 SQ M
Duplex Penthouse
4 suites
Price R$ 2.200.000
Price per SQ M: R$ 8.764
First Sub-Page
This is about the Condominium which is called "Gentle Palm Residences" with the following bullets
*Family friendly and safe
*Direct access to the beach
*Many amenities like pool, football court, gym, sauna
There should be some photos of the condominium and a link to the site of the condominium ( www.gprvx.com )
Second Sub-page
This is about the apartment. It should list in bullets the features of the apartment and then have a photo gallery of the view and various rooms. I have attached sample photos but will eventually have to use more photos.
Apartment Features
Price: R$ 2.220.000
251 m2 Duplex Penthouse
4 suites
maids room with bath
guest bathroom
living room
dinning room
Terrace with heated pool for year round use
Veranda
As mentioned above I am open to all designs and navigation so feel free to be creative. The important thing is catch peoples attention and get the message across in a few seconds, which is that there is an apartment for sale at this price with these features in this location. I will then use brightlist promoter and SEO to get people to the site.
Thanks
Target Market(s)
Men and Women from 30-60 years of age.
Industry/Entity Type
Apartment

```html
<!DOCTYPE html>
<html lang="en">
<head>
<meta charset="utf-8">
<title>Gentle Palm Residences</title>
<link href="https://fonts.googleapis.com/css2?family=Open+Sans:wght@400;600;700&family=Arimo:wght@400;700&display=swap" rel="stylesheet">
<style>
:root{
  --dark:#2f3a47;
  --dark-2:#27313c;
  --blue:#1f7fe0;
  --blue-dark:#1466c4;
  --link:#1b6fc2;
  --title:#1a5fa3;
  --page:#e8e8ea;
  --text:#333;
  --muted:#666;
  --line:#d5d5d8;
  --white:#fff;
  --green:#6cbf2a;
}
*{box-sizing:border-box;margin:0;padding:0}
html,body{width:947px;height:1200px;overflow:hidden}
body{position:relative;background:var(--page);font-family:"Open Sans",sans-serif;color:var(--text)}
.abs{position:absolute}
.site-header{left:0;top:0;width:947px;height:80px;background:linear-gradient(#35414f,var(--dark-2))}
.brand{left:110px;top:6px;color:#fff;font-family:"Arimo",sans-serif;font-weight:700;font-size:25px;line-height:31px;letter-spacing:2.5px}
.social-dots{left:672px;top:33px;display:flex;gap:9px}
.social-dots span{width:19px;height:19px;border-radius:50%;background:#5c6672}
.main-nav{left:0;top:80px;width:947px;height:35px;background:#fff;border-bottom:1px solid #ccc}
.main-nav ul{list-style:none;display:flex;position:absolute;left:113px;top:8px}
.main-nav li{font-size:13px;line-height:19px;padding:0 15px;border-left:1px solid #999;color:#222}
.main-nav li:first-child{border:none;padding:0 8px 0 0}
.main-nav li.active a{background:var(--blue);color:#fff;border-radius:3px;padding:1px 6px;display:inline-block;line-height:17px}
.search-box{left:655px;top:86px;width:190px;height:22px;border:1px solid #bbb;border-radius:2px;font-size:12px;color:#999;padding:2px 9px}
.search-box svg{position:absolute;right:4px;top:2px}
.hero{left:102px;top:132px;width:514px;height:275px;background:#fff;box-shadow:0 1px 4px rgba(0,0,0,.3);border-radius:3px}
.hero-photo{position:absolute;left:4px;top:5px;width:506px;height:266px;background:linear-gradient(100deg,#8a7462,#d9cfc2 45%,#4a3a2e 70%,#c8ccd0)}
.hero-caption{position:absolute;left:4px;bottom:4px;width:506px;height:65px;background:rgba(0,0,0,.55);color:#fff}
.hero-caption h2{position:absolute;left:10px;top:6px;font-size:14px;font-weight:600}
.hero-caption .price{position:absolute;right:10px;top:6px;font-size:14px;font-weight:600}
.hero-caption p{position:absolute;left:10px;top:30px;font-size:9px;line-height:11px;width:360px}
.btn{background:var(--blue);color:#fff;border-radius:3px;font-size:10px;text-align:center}
.hero-caption .btn{position:absolute;right:10px;top:40px;width:62px;height:18px;line-height:18px}
.hero-arrow{width:18px;height:18px;background:rgba(255,255,255,.85)}
.finder{left:616px;top:141px;width:229px;height:262px;background:#fff;border-radius:0 3px 3px 0;box-shadow:0 1px 3px rgba(0,0,0,.2)}
.finder h3{height:33px;background:linear-gradient(#3390ec,var(--blue-dark));color:#fff;font-weight:400;font-size:15px;line-height:33px;padding-left:17px;border-radius:0 3px 0 0}
.field{position:absolute;left:25px;font-size:11px;color:#333}
.select{position:absolute;left:81px;width:131px;height:21px;border:1px solid #ccc;border-radius:2px;background:#fafafa}
.select::after{content:"";position:absolute;right:7px;top:8px;border:4px solid transparent;border-top:5px solid #333}
.select::before{content:"";position:absolute;right:21px;top:0;height:19px;border-left:1px solid #ccc}
.range{position:absolute;left:33px;top:218px;width:172px;height:8px;border:1px solid #ccc;border-radius:4px;background:#eee}
.range .fill{position:absolute;left:20px;width:84px;height:6px;background:#bbb}
.range .knob{position:absolute;top:-5px;width:13px;height:15px;background:#fff;border:1px solid #aaa;border-radius:2px}
.finder .btn{position:absolute;left:151px;top:237px;width:61px;height:19px;line-height:19px;font-size:11px}
.tabs{left:99px;top:424px;width:749px;height:36px;border-bottom:2px solid var(--blue)}
.tab{position:absolute;top:0;height:35px;font-size:11px;line-height:35px;padding:0 7px;color:#666}
.tab.active{background:var(--blue);color:#fff;font-weight:600;left:0;width:87px}
.gallery{left:99px;top:461px;width:749px;height:226px;background:#fff}
.card{position:absolute;top:16px;width:153px}
.card .thumb{height:116px}
.card h4{font-weight:400;font-size:13px;color:var(--title);margin:5px 0 2px 2px}
.card p{font-family:"Arimo",sans-serif;font-size:7.5px;line-height:11px;color:#333;margin-left:2px}
.card a{display:block;font-size:9px;color:var(--link);margin:8px 0 0 1px}
.round-arrow{width:22px;height:30px;background:#f2f2f2;border-radius:50%;color:var(--blue);font-weight:700;font-size:13px;text-align:center;line-height:30px}
.newsletter{left:98px;top:710px;width:217px;height:129px;background:#fff;border-radius:3px}
.newsletter h3{position:absolute;left:6px;top:13px;font-size:16px;font-weight:600;color:#1f3f6e}
.newsletter p{position:absolute;left:7px;top:42px;width:200px;font-family:"Arimo",sans-serif;font-size:8.5px;line-height:12px;color:#222}
.newsletter .email{position:absolute;left:5px;top:85px;width:136px;height:25px;border:1px solid #9cc7e6;background:#eef6fc;font-size:9.5px;line-height:23px;padding-left:6px;color:#555}
.newsletter .send{position:absolute;left:140px;top:85px}
.promo{left:98px;top:848px;width:217px;height:118px;border-radius:3px;overflow:hidden;z-index:2;background:linear-gradient(#4a9ad8,#9fd0f0 60%,#e8dcc0)}
.promo .headline{position:absolute;left:9px;top:5px;color:#fff;font-family:"Arimo",sans-serif;font-weight:700;font-size:16px}
.promo .headline small{font-size:11px}
.promo .sub{position:absolute;left:9px;top:28px;color:#fff;font-family:"Arimo",sans-serif;font-weight:700;font-size:9.5px;line-height:12.5px}
.promo .deals{position:absolute;left:91px;top:88px;width:108px;height:21px;background:linear-gradient(#ffa320,#e86b00);border-radius:3px;color:#fff;font-family:"Arimo",sans-serif;font-weight:700;font-size:12px;text-align:center;line-height:21px}
.feature{position:absolute;top:709px;width:165px;z-index:2}
.feature h4{font-weight:400;font-size:13px;color:#222}
.feature .photo{margin-top:5px;height:107px;border:2px solid #fff;box-shadow:0 0 2px rgba(0,0,0,.2)}
.feature p{font-size:8.3px;line-height:16px;color:#444;margin:9px 0 0 2px;white-space:nowrap}
.feature p span{color:#ddd}
.feature a{display:block;font-size:9.5px;color:var(--link);margin:4px 0 0 2px}
.fade{left:0;top:940px;width:947px;height:45px;background:linear-gradient(var(--page),#ddd8d0);z-index:0}
.site-footer{left:0;top:985px;width:947px;height:215px;background:var(--dark)}
.foot-list{position:absolute;list-style:none;color:#fff;font-size:10.5px}
.foot-list li{height:23.7px}
.foot-list li::before{content:"• ";color:#778}
.site-footer h4{position:absolute;color:#fff;font-weight:400;font-size:15px}
.follow{position:absolute;left:468px;display:flex;align-items:center;gap:9px;color:#fff;font-size:10.5px}
.follow i{width:23px;height:23px;background:#55606d;border-radius:2px;display:block}
.cin{position:absolute;left:675px;width:172px;height:16px;background:#fff;border:1px solid #ccc;font-size:8px;color:#999;padding-left:24px;line-height:14px}
.cin svg{position:absolute;left:7px;top:3px}
.cin.msg{height:40px;padding:5px 12px}
.send-msg{position:absolute;left:674px;top:1153px;width:113px;height:22px;background:linear-gradient(#fff,#ddd);border:1px solid #aaa;font-size:9.5px;text-align:center;line-height:20px;color:#333}
</style>
</head>
<body>
<div class="abs fade"></div>
<header class="abs site-header">
  <div class="abs brand">Gentle Palm<br>Residences</div>
  <div class="abs social-dots"><span></span><span></span><span></span><span></span><span></span><span></span></div>
</header>
<nav class="abs main-nav">
  <ul>
    <li class="active"><a>Home</a></li>
    <li>About Condominium</li>
    <li>About Apartment</li>
    <li>Contact Us</li>
  </ul>
  <div class="abs search-box" style="top:6px">Search
    <svg width="18" height="17" viewBox="0 0 18 17"><circle cx="7" cy="7" r="5.5" fill="none" stroke="#888" stroke-width="2"/><path d="M11 11l5 5" stroke="#888" stroke-width="3"/></svg>
  </div>
</nav>

<section class="abs hero">
  <div class="hero-photo" role="img" aria-label="Penthouse living room with paintings, staircase and large windows"></div>
  <div class="abs hero-arrow" style="left:5px;top:120px"><svg width="18" height="18"><path d="M12 4L5 9l7 5z" fill="#333"/></svg></div>
  <div class="abs hero-arrow" style="left:491px;top:120px;background:none"><svg width="18" height="18"><path d="M6 4l7 5-7 5z" fill="#fff"/></svg></div>
  <div class="hero-caption">
    <h2>Duplex Penthouse 4 suites</h2>
    <div class="price">Price R$ 2.200.000</div>
    <p>This is the landing page and should make it obvious that there is an apartment for sale in Barra Da Tijuca, Rio De Janeiro with the following attributes</p>
    <div class="btn">Read more</div>
  </div>
</section>

<aside class="abs finder">
  <h3>Find Your Apartment</h3>
  <span class="field" style="top:51px">Type</span><div class="select" style="top:48px"></div>
  <span class="field" style="top:78px">Beds</span><div class="select" style="top:75px"></div>
  <span class="field" style="top:110px">Baths</span><div class="select" style="top:107px"></div>
  <span class="field" style="top:142px">City</span><div class="select" style="top:139px"></div>
  <span class="field" style="top:171px">Status</span><div class="select" style="top:168px"></div>
  <span class="field" style="top:197px;left:26px">Price Range</span><span class="field" style="top:197px;left:101px">1000-3000</span>
  <div class="range"><div class="fill"></div><div class="knob" style="left:12px"></div><div class="knob" style="left:80px"></div></div>
  <div class="btn">Search</div>
</aside>

<div class="abs tabs">
  <div class="tab active">Condominium</div>
  <div class="tab" style="left:91px">The Apartment</div>
</div>
<section class="abs gallery">
  <div class="abs round-arrow" style="left:-6px;top:80px">‹</div>
  <div class="abs round-arrow" style="left:733px;top:80px">›</div>
  <div class="card" style="left:40px"><div class="thumb" role="img" aria-label="Apartment hallway with dining area" style="background:linear-gradient(90deg,#6b6158,#cfc8bd,#8a7460)"></div><h4>Duplex Penthouse</h4><p>4 suites,<br>Price R$ 2.200.000<br>Price per SQ M: R$ 8.764</p><a>Click to go »</a></div>
  <div class="card" style="left:212px"><div class="thumb" role="img" aria-label="Terrace with heated pool and lounge chairs" style="background:linear-gradient(#eee,#a33 40%,#3a8fc0 75%,#b7836a)"></div><h4>Duplex Penthouse</h4><p>4 suites,<br>Price R$ 2.200.000<br>Price per SQ M: R$ 8.764</p><a>Click to go »</a></div>
  <div class="card" style="left:384px"><div class="thumb" role="img" aria-label="View of mountains over the neighbourhood at sunset" style="background:linear-gradient(#c9d4d8,#a89a78 45%,#2e3a1e)"></div><h4>Duplex Penthouse</h4><p>4 suites,<br>Price R$ 2.200.000<br>Price per SQ M: R$ 8.764</p><a>Click to go »</a></div>
  <div class="card" style="left:556px"><div class="thumb" role="img" aria-label="Condominium pool seen from above" style="background:radial-gradient(#6fc3c8,#3e7a70 55%,#2a3a1c)"></div><h4>Duplex Penthouse</h4><p>4 suites,<br>Price R$ 2.200.000<br>Price per SQ M: R$ 8.764</p><a>Click to go »</a></div>
</section>

<section class="abs newsletter">
  <h3>Newsletter</h3>
  <p>Join our newsletter to find the finest selection of personally inspected Holiday Cottages.</p>
  <div class="email">Your e-mail</div>
  <svg class="send" width="68" height="25" viewBox="0 0 68 25"><path d="M0 0h56l12 12.5L56 25H0z" fill="#6cbf2a"/><text x="5" y="17" fill="#fff" font-family="Arimo,sans-serif" font-weight="700" font-size="12">Send</text></svg>
</section>
<section class="abs promo" role="img" aria-label="Family holiday offer with beach scene">
  <div class="headline">Family offers <small>from</small> £199</div>
  <div class="sub">Including Majorca,<br>Gran Canaria, and<br>Orlando</div>
  <div class="deals">View deals »</div>
</section>

<article class="feature" style="left:333px"><h4>Family Friendly &amp; Safe</h4><div class="photo" role="img" aria-label="Condominium patio with umbrellas and tables" style="background:linear-gradient(#e4e8ec,#8a9a8a 50%,#b8b8b8)"></div><p>Lorem Ipsum is simply dummy text of<br>the printing and typesetting industry.<br>Lorem Ipsum has been the industry's<br>standard dummy <span>unchanged.</span></p><a>Read more</a></article>
<article class="feature" style="left:504px"><h4>The Beach</h4><div class="photo" role="img" aria-label="Beach and seafront towers below mountains" style="background:linear-gradient(#9fb0c0,#6e7a80 35%,#a0a4a8 65%,#e8eef0)"></div><p>Lorem Ipsum is simply dummy text of<br>the printing and typesetting industry.<br>Lorem Ipsum has been the industry's<br>standard dummy <span>unchanged.</span></p><a>Read more</a></article>
<article class="feature" style="left:674px"><h4>Pool, Football</h4><div class="photo" role="img" aria-label="Condominium pool seen from above" style="background:radial-gradient(#6fc3c8,#3e7a70 55%,#2a3a1c)"></div><p>Lorem Ipsum is simply dummy text of<br>the printing and typesetting industry.<br>Lorem Ipsum has been the industry's<br>standard dummy <span>unchanged.</span></p><a>Read more</a></article>

<footer class="abs site-footer">
  <ul class="foot-list" style="left:110px;top:32px"><li>Home</li><li>AboutUs</li><li>Service</li><li>Products</li><li>Contact Us</li></ul>
  <ul class="foot-list" style="left:280px;top:32px"><li>Lorem Ipsum</li><li>Lorem Ipsum</li><li>Lorem Ipsum</li><li>Lorem Ipsum</li><li>Lorem Ipsum</li><li>Lorem Ipsum</li></ul>
  <h4 style="left:466px;top:26px">Follow Us</h4>
  <div class="follow" style="top:52px"><i></i>Follow us on Friendloop</div>
  <div class="follow" style="top:80px"><i></i>Follow us on Chirpline</div>
  <div class="follow" style="top:107px"><i></i>Follow us on Workweave</div>
  <div class="follow" style="top:135px"><i></i>Follow us on Streamly</div>
  <h4 style="left:671px;top:26px">Contact us</h4>
</footer>
<div class="cin" style="top:1037px"><svg width="10" height="9"><circle cx="5" cy="3" r="2.5" fill="#999"/><path d="M0 9a5 4 0 0 1 10 0z" fill="#999"/></svg>Name</div>
<div class="cin" style="top:1060px"><svg width="11" height="8"><rect x=".5" y=".5" width="10" height="7" fill="none" stroke="#999"/><path d="M.5.5l5 4 5-4" fill="none" stroke="#999"/></svg>Enter your email here</div>
<div class="cin" style="top:1083px"><svg width="10" height="10"><path d="M1 9l2-4 6-5 1 1-5 6z" fill="#e2a23a"/></svg>Subject</div>
<div class="cin msg" style="top:1105px">What's Up?</div>
<div class="send-msg">Send Message</div>
</body>
</html>
```